International Employee Benefits

Create website including logo for Dunmore Global
Specialising in setting up and managing employee benefits for multi-national companies
Should be professional and simple to navigate
Updates

Company name is Dunmore Global

Please ensure the following is adhered to :

Page size - 950 pixels wide

If you plan to use a texture or picture background please ensure these are tiled so that the left edge matches the right edge like wallpaper.

The home page should have the logo at the top left of the screen followed by tabs "About Us", "Resources" "Expertise" "References" "Contact Us"
Perhaps there can also be an image on the home page, something that signifies global success??

The wording on the home page should be:

 Dunmore Global brings a results oriented approach partnering with clients in mapping out customized strategies that meet their international objectives that save time and money and leaves an established process in place.  The client is supported with a high touch, one point of contact, that bring solutions to complex problems

 

Target Market(s)

Companies - HR and Finance

Industry/Entity Type

Employee

Requirements
Must have
• Map of world or globe

```html
<!DOCTYPE html>
<html lang="en">
<head>
<meta charset="utf-8">
<title>Dunmore Global – International Employee Benefits</title>
<link href="https://fonts.googleapis.com/css2?family=Oswald:wght@300;400&family=Open+Sans:wght@300;400;600;700&family=Arimo:wght@400&display=swap" rel="stylesheet">
<style>
:root{
  --ink:#555;
  --ink-soft:#888;
  --navy:#1d4c8c;
  --blue:#2a63b0;
  --blue-dark:#163f78;
  --orange:#f26b0f;
  --orange-deep:#ec5a05;
  --footer:#222;
  --footer-line:#3a3a3a;
  --field:#141414;
  --footer-text:#d8d8d8;
  --link:#2f6ec2;
}
*{margin:0;padding:0;box-sizing:border-box}
html,body{width:848px;height:1200px;overflow:hidden;background:#fff}
body{position:relative;font-family:"Open Sans",sans-serif;color:var(--ink)}
.abs{position:absolute}

.logo{left:29px;top:24px;font-family:"Open Sans",sans-serif;font-weight:300;font-size:27px;letter-spacing:1px;color:#999;text-transform:uppercase}
.nav{right:29px;top:38px;display:flex;gap:26px;font-family:"Oswald",sans-serif;font-weight:300;font-size:13px;color:#777;text-transform:uppercase}
.header-rule{left:29px;top:62px;width:790px;height:1px;background:#ccc}

.hero-map{left:29px;top:100px;width:478px;height:316px;background:#fff;border:1px solid #ddd;box-shadow:3px 4px 4px rgba(0,0,0,.35);padding:18px 20px}
.hero-map .fill{width:100%;height:100%;background:radial-gradient(ellipse at 40% 45%,#1e7cc9 0%,#1563b0 45%,#d8e8f6 80%,#fff 100%)}

.side-column{left:519px;top:416px;width:329px;height:402px;background:linear-gradient(90deg,#f0f0f0 0%,#fff 18%)}
.side-top-shade{left:519px;top:416px;width:329px;height:30px;background:linear-gradient(180deg,#e9e9e9,#fff)}

.motto{left:519px;top:100px;width:300px;height:316px;border:8px solid var(--orange);border-image:linear-gradient(180deg,#f58a1c,var(--orange-deep)) 1;background:#fff;padding:40px 0 0 37px}
.motto h2{font-family:"Arimo",sans-serif;font-weight:400;font-size:42px;line-height:42px;color:var(--navy)}
.motto p{margin-top:24px;font-weight:300;font-size:15px;line-height:19px;color:#888}

.btn{display:inline-block;font-family:"Oswald",sans-serif;font-size:16px;color:#fff;text-transform:uppercase;background:linear-gradient(180deg,#2f64ad,var(--blue-dark));border-bottom:2px solid #0e2f5c;width:82px;height:40px;line-height:40px;text-align:center;letter-spacing:-.2px}
.motto .btn{position:absolute;left:49px;top:223px}

.main-title{left:31px;top:452px;font-family:"Arimo",sans-serif;font-size:33px;color:#666}
.intro{left:32px;top:510px;width:450px;font-size:11px;line-height:17.5px;color:#555}
.intro-btn{left:31px;top:603px}

.box-bar{left:519px;width:300px;height:34px;border-radius:0 9px 9px 0;background:linear-gradient(90deg,#1e4d8e,#2c64b0);font-family:"Oswald",sans-serif;font-size:18px;line-height:33px;color:#fff;padding-left:29px;letter-spacing:-.3px}
.thumb{left:548px;width:75px;height:67px;border:1px solid #ccc;padding:2px}
.thumb .fill{width:100%;height:100%}
.thumb.people .fill{background:linear-gradient(180deg,#f2f2f2,#2a2a2a)}
.thumb.team .fill{background:linear-gradient(180deg,#e8f2fb,#5aa6e0)}
.box-text{left:642px;width:170px;font-size:11px;line-height:15px;color:#444}
.box-link{left:643px;font-family:"Oswald",sans-serif;font-weight:300;font-size:13px;color:#777;text-transform:uppercase}

.footer{left:0;top:818px;width:848px;height:382px;background:var(--footer);box-shadow:inset 0 8px 10px rgba(0,0,0,.5)}
.col{top:850px}
.col h3{font-family:"Arimo",sans-serif;font-weight:400;font-size:25px;color:var(--link)}
.col .lede{margin-top:12px;font-size:12.5px;color:var(--footer-text);padding-bottom:8px;border-bottom:1px solid var(--footer-line);width:240px}
.col-contact{left:31px}
.col-testimonials{left:303px}
.col-news{left:577px}
.field{position:absolute;left:30px;width:175px;background:var(--field);border-radius:3px;font-size:12px;color:#888;padding:3px 7px}
.send{left:32px;top:1103px;font-family:"Oswald",sans-serif;font-weight:300;font-size:13px;color:#999}
.entry{font-size:12.5px;line-height:20px;color:#ccc}
.entry b{display:block;font-weight:700;color:#e5e5e5}
.entry .meta{display:block;font-weight:700;color:#e5e5e5}
.entry a{display:block;font-weight:700;color:var(--link);text-decoration:none}
.entry p{line-height:15px;margin-top:2px}
.news-more{left:579px;top:1103px;font-family:"Oswald",sans-serif;font-weight:300;font-size:13px;color:#999}

.footer-rule{left:0;top:1168px;width:848px;height:1px;background:var(--footer-line)}
.copyright{left:31px;top:1176px;font-size:12.5px;color:#888}
.copyright span{color:var(--link)}
.footer-nav{right:31px;top:1179px;display:flex;gap:12px;font-family:"Oswald",sans-serif;font-weight:300;font-size:10px;color:#999;text-transform:uppercase}
.footer-nav i{font-style:normal;color:#666}
</style>
</head>
<body>

<div class="abs logo">Dunmore Global</div>
<nav class="abs nav"><span>About Us</span><span>Resources</span><span>Expertise</span><span>Refeerences</span><span>Contact Us</span></nav>
<div class="abs header-rule"></div>

<div class="abs hero-map"><div class="fill" role="img" aria-label="Blue map of the world"></div></div>

<div class="abs side-column"></div>
<div class="abs side-top-shade"></div>

<section class="abs motto">
  <h2>Motto<br>Goes Here</h2>
  <p>Usu impedit qualisque<br>persequeris te, est timeam</p>
  <span class="btn">Read More</span>
</section>

<h1 class="abs main-title">Main Title Goes Here</h1>
<p class="abs intro">Dunmore Global brings a results oriented approach partnering with clients in mapping out customized strategies that meet their international objectives that save time and money and leaves an established process in place. The client is supported with a high touch, one point of contact, that bring solutions to complex problems</p>
<span class="abs btn intro-btn">Read More</span>

<div class="abs box-bar" style="top:444px">Box Title Goes Here</div>
<div class="abs thumb people" style="top:506px"><div class="fill" role="img" aria-label="Photo of a smiling business team"></div></div>
<p class="abs box-text" style="top:503px">Mel agam habemus eu,<br>ridens mollis ut duo. Mundi</p>
<span class="abs box-link" style="top:546px">Read More</span>

<div class="abs box-bar" style="top:617px">Box Title Goes Here</div>
<div class="abs thumb team" style="top:680px"><div class="fill" role="img" aria-label="Silhouettes of people standing on puzzle pieces"></div></div>
<p class="abs box-text" style="top:677px">Mel agam habemus eu,<br>ridens mollis ut duo. Mundi</p>
<span class="abs box-link" style="top:720px">Read More</span>

<footer class="abs footer"></footer>

<div class="abs col col-contact"><h3>Contact Us</h3><p class="lede">Use the form below to send us a message</p></div>
<div class="field" style="top:936px;height:20px">Name</div>
<div class="field" style="top:966px;height:20px">E-mail</div>
<div class="field" style="top:996px;height:90px">Message</div>
<span class="abs send">SEND</span>

<div class="abs col col-testimonials"><h3>Testimonials</h3><p class="lede">Some comments from our clients</p></div>
<div class="abs entry" style="left:303px;top:920px"><b>Mr. Alan Reeve</b><span class="meta">Jan 17th 2013</span><p>Mei et audire admodum feugait.</p></div>
<div class="abs entry" style="left:303px;top:994px"><b>Mr. Alan Reeve</b><span class="meta">Aug 17th 2012</span><p>Mei et audire admodum feugait.</p></div>
<div class="abs entry" style="left:303px;top:1069px"><b>Mr. Alan Reeve</b><span class="meta">Aug 17th 2012</span><p>Mei et audire admodum feugait.</p></div>

<div class="abs col col-news"><h3>Latest News</h3><p class="lede">Latest from the Blog</p></div>
<div class="abs entry" style="left:578px;top:920px;width:240px"><a>News Title Here</a><span class="meta">03.01.2013.</span><p>Mei et audire admodum feugait. Mei tincidunt elaboraret no. An duo regione</p></div>
<div class="abs entry" style="left:578px;top:1006px;width:240px"><a>News Title Here</a><span class="meta">03.11.2012.</span><p>Mei et audire admodum feugait. Mei tincidunt elaboraret no. An duo regione</p></div>
<span class="abs news-more">READ MORE</span>

<div class="abs footer-rule"></div>
<p class="abs copyright">Copyright 2013 - <span>Dunmore Global</span> - All Rights Reserved</p>
<nav class="abs footer-nav"><span>About Us</span><i>|</i><span>Resources</span><i>|</i><span>Expertise</span><i>|</i><span>Refeerences</span><i>|</i><span>Contact Us</span></nav>

</body>
</html>
```